Willowmere Counseling (Endure - Mend - Flourish) - Double Sided Business Card

I would like a 2-sided business card. Front: Matte Black or Navy with Logo & Tagline. Back: Name, Address, Phone Number, Email, & Website (maybe would like to include a small map pin-pointing location); Prefer front to be a gold/silver foil (iridescent); Back prefer white or light colored background with lettering that is easy to read and simple

Target Market(s)

Individuals & Couples (13 y.o. - ALL Adults); High end clientele

Industry/Entity Type

Licensed Professional Counselor (Mental Health)

Contact Information for Business Card

Name: Willowmere Counseling; Tagline: Endure - Mend - Flourish; Address: 3870 N. Garrick Ave., Suite 214, Fort Worth, TX 76132; Phone: (214) 555-0187; Website: www.WillowmereCounseling.example

Font styles to use
Serif

Requirements
Must have
• Logo on Front (Large) prefer gold/silver foil on a matte dark color (i.e. black, navy, etc.); Back of Card: All other relevant information

```html
<!DOCTYPE html>
<html lang="en">
<head>
<meta charset="utf-8">
<title>Willowmere Counseling – Business Card</title>
<link href="https://fonts.googleapis.com/css2?family=Cinzel:wght@400;600&family=Montserrat:wght@400;500;700&display=swap" rel="stylesheet">
<style>
  :root {
    --page: #ffffff;
    --ink-dark: #0b0f13;
    --ink-dark-2: #121416;
    --gold: #d8b84f;
    --silver: #8a8b8d;
    --text: #1a1a1a;
    --rule: #6f6f6f;
    --card-light: #ffffff;
    --faint: #f3f3f3;
  }
  * { box-sizing: border-box; margin: 0; padding: 0; }
  html, body { width: 687px; height: 1200px; overflow: hidden; background: var(--page); }
  .canvas {
    width: 687px; height: 1200px;
    display: flex; flex-direction: column; align-items: center; justify-content: center;
    gap: 34px;
  }
  .card {
    position: relative; width: 600px; height: 343px; overflow: hidden;
    box-shadow: 0 2px 8px rgba(0,0,0,.25);
  }

  /* Front */
  .card-front {
    background: linear-gradient(180deg, var(--ink-dark) 0%, var(--ink-dark-2) 100%);
    display: flex; flex-direction: column; align-items: center;
  }
  .card-front .backdrop-circle {
    position: absolute; right: -40px; top: 0; width: 270px; height: 270px;
    border-radius: 50%; background: rgba(255,255,255,.025);
  }
  .brand-mark {
    width: 64px; height: 64px; border-radius: 50%;
    border: 5px solid var(--gold); margin-top: 62px;
  }
  .brand-name {
    font-family: "Cinzel", serif; font-weight: 600; color: var(--gold);
    letter-spacing: .5px; line-height: 1;
  }
  .card-front .brand-name { font-size: 27px; margin-top: 26px; }
  .tagline {
    font-family: "Cinzel", serif; font-weight: 400; color: var(--gold);
    display: flex; align-items: center; white-space: nowrap;
  }
  .tagline::before, .tagline::after {
    content: ""; height: 2px; background: var(--silver);
  }
  .card-front .tagline { font-size: 15px; margin-top: 12px; gap: 10px; }
  .card-front .tagline::before, .card-front .tagline::after { width: 46px; }
  .front-web {
    font-family: "Montserrat", sans-serif; font-size: 10.5px; color: var(--silver);
    letter-spacing: .3px; margin-top: 38px;
  }

  /* Back */
  .card-back { background: var(--card-light); border-bottom: 6px solid var(--gold); }
  .card-back .backdrop-circle {
    position: absolute; left: 0; top: -10px; width: 270px; height: 270px;
    border-radius: 50%; background: var(--faint);
  }
  .back-brand {
    position: absolute; right: 22px; top: 22px;
    display: flex; flex-direction: column; align-items: center;
  }
  .back-brand .brand-mark { width: 54px; height: 54px; border-width: 4px; margin-top: 0; }
  .back-brand .brand-name { font-size: 17px; margin-top: 14px; }
  .back-brand .tagline { font-size: 10px; margin-top: 7px; gap: 7px; }
  .back-brand .tagline::before, .back-brand .tagline::after { width: 30px; height: 1.5px; }

  .holder {
    position: absolute; left: 20px; top: 210px; right: 20px;
    display: flex; align-items: center; gap: 8px;
  }
  .holder-name {
    font-family: "Montserrat", sans-serif; font-weight: 700; font-size: 21px;
    color: var(--text); letter-spacing: .5px; white-space: nowrap;
  }
  .holder-rule { flex: 1; height: 1.5px; background: var(--rule); margin-left: 8px; }

  .contact-list {
    position: absolute; left: 20px; top: 255px; list-style: none;
    font-family: "Montserrat", sans-serif; font-size: 11.5px; color: var(--text);
  }
  .contact-list li { display: flex; align-items: center; gap: 12px; height: 24px; }
  .icon { width: 15px; height: 15px; flex: none; fill: var(--gold); }

  .address {
    position: absolute; right: 22px; top: 262px;
    display: flex; gap: 14px;
    font-family: "Montserrat", sans-serif; font-size: 11.5px; line-height: 19px; color: var(--text);
  }
  .address .icon { margin-top: 2px; }
</style>
</head>
<body>
<main class="canvas">

  <section class="card card-front" aria-label="Card front">
    <div class="backdrop-circle"></div>
    <div class="brand-mark"></div>
    <div class="brand-name">WILLOWMERE COUNSELING</div>
    <div class="tagline">ENDURE - MEND - FLOURISH</div>
    <div class="front-web">www.willowmerecounseling.example</div>
  </section>

  <section class="card card-back" aria-label="Card back">
    <div class="backdrop-circle"></div>

    <div class="back-brand">
      <div class="brand-mark"></div>
      <div class="brand-name">WILLOWMERE COUNSELING</div>
      <div class="tagline">ENDURE - MEND - FLOURISH</div>
    </div>

    <div class="holder">
      <svg class="icon" viewBox="0 0 16 16" aria-hidden="true"><circle cx="8" cy="5" r="3.6"/><path d="M1.5 16c0-4 2.9-6.3 6.5-6.3s6.5 2.3 6.5 6.3z"/></svg>
      <span class="holder-name">MARCUS HALE</span>
      <span class="holder-rule"></span>
    </div>

    <ul class="contact-list">
      <li>
        <svg class="icon" viewBox="0 0 16 16" aria-hidden="true"><path d="M3.3 1.2l2.4 2.9-1.4 1.6c.9 2 2.3 3.5 4.4 4.6l1.6-1.4 2.9 2.4-1.6 2.5C6.5 13.3 2.3 9 .9 3z"/></svg>
        (214) 555-0187
      </li>
      <li>
        <svg class="icon" viewBox="0 0 16 16" aria-hidden="true"><path d="M1 3h14v1.2L8 9 1 4.2z"/><path d="M1 5.8l7 4.8 7-4.8V13H1z"/></svg>
        hello@willowmerecounseling.example
      </li>
      <li>
        <svg class="icon" viewBox="0 0 16 16" aria-hidden="true"><path d="M8 1a7 7 0 1 0 0 14A7 7 0 0 0 8 1zm0 1.4c.8.8 1.5 2.3 1.7 4.1H6.3C6.5 4.7 7.2 3.2 8 2.4zM2.5 7.3h2.9c0 1.6.3 3 .9 4.2a5.6 5.6 0 0 1-3.8-4.2zm0-1h0a5.6 5.6 0 0 1 3.8-3.8c-.6 1.1-.9 2.4-.9 3.8zm5.5 7.3c-.8-.8-1.5-2.3-1.7-4.3h3.4c-.2 2-.9 3.5-1.7 4.3zm1.7-1.1c.6-1.2.9-2.6.9-4.2h2.9a5.6 5.6 0 0 1-3.8 4.2zm.9-5.2c0-1.4-.3-2.7-.9-3.8a5.6 5.6 0 0 1 3.8 3.8z"/></svg>
        www.willowmerecounseling.example
      </li>
    </ul>

    <div class="address">
      <svg class="icon" viewBox="0 0 16 16" aria-hidden="true"><path d="M8 0a5.5 5.5 0 0 0-5.5 5.5C2.5 9.6 8 16 8 16s5.5-6.4 5.5-10.5A5.5 5.5 0 0 0 8 0zm0 7.8a2.3 2.3 0 1 1 0-4.6 2.3 2.3 0 0 1 0 4.6z"/></svg>
      <address style="font-style:normal">3870 N. Garrick Ave.,<br>Suite 214, Fort Worth,<br>TX 76132</address>
    </div>
  </section>

</main>
</body>
</html>
```